Nonprofit K-8 Korbane School. Elementary education ( please google Korbane Schools)

We are a nonprofit Korbane School in the U.S.
We need to advertise our school using yard signs. The information should be easy to see from a distance. Clear and concise, using large print without additional design outside of the logo itself. It should have our logo as the header, with the following text centered below the logo:
Open House!
Feb 10th, March 10th and April 21st.
Call 555 014-2967 for more information

Target Market(s)

Parents of children between ages of 5 yrs to 13yrs old

Industry/Entity Type

School

Other font styles liked:
• Formal436bt

Colors
ec1f27
ffffff

Requirements
Must have
• It must have our uploaded logo as the header, and the following information below using the font Formal436bt:
• Open House!
• Feb 10th, March 10th and April 21st.
• Call 555 014-2967 for more information
Should not have
• Any other color but the red and white indicated on our logo

```html
<!DOCTYPE html>
<html lang="en">
<head>
<meta charset="utf-8">
<title>Korbane School – Open House Yard Sign</title>
<link href="https://fonts.googleapis.com/css2?family=Marcellus&display=swap" rel="stylesheet">
<style>
  :root {
    --brand-red: #ec1f27;
    --brand-red-deep: #b20d18;
    --brand-white: #ffffff;
    --page-bg: #e6e6e6;
    --text-shadow: rgba(90, 0, 6, 0.45);
  }
  * { margin: 0; padding: 0; box-sizing: border-box; }
  html, body {
    width: 1200px;
    height: 1200px;
    overflow: hidden;
    background: var(--page-bg);
  }
  body {
    display: flex;
    align-items: center;
    justify-content: center;
    font-family: "Marcellus", serif;
  }
  .yard-sign {
    position: relative;
    width: 1100px;
    height: 826px;
    overflow: hidden;
  }
  .sign-artwork {
    position: absolute;
    inset: 0;
    width: 100%;
    height: 100%;
  }
  .sign-content {
    position: absolute;
    inset: 0;
    color: var(--brand-white);
    text-align: center;
  }
  .sign-content > * {
    position: absolute;
    left: 0;
    right: 0;
  }
  .school-name {
    top: 81px;
    font-size: 38px;
    line-height: 38px;
    letter-spacing: 0.5px;
  }
  .headline {
    top: 168px;
    font-size: 86px;
    line-height: 86px;
    font-weight: 400;
    letter-spacing: 1px;
    text-shadow: 2px 3px 3px var(--text-shadow);
  }
  .date-icon {
    top: 264px;
    left: 510px;
    right: auto;
    width: 80px;
    height: 80px;
  }
  .dates {
    top: 355px;
    list-style: none;
    font-size: 48px;
    line-height: 62px;
  }
  .dates sup {
    font-size: 0.55em;
    vertical-align: 0.75em;
    line-height: 0;
  }
  .phone-number {
    top: 681px;
    font-size: 98px;
    line-height: 98px;
    color: var(--brand-red-deep);
    letter-spacing: 2px;
  }
</style>
</head>
<body>
  <section class="yard-sign" aria-label="Korbane School open house sign">
    <svg class="sign-artwork" viewBox="0 0 1100 826" aria-hidden="true">
      <defs>
        <linearGradient id="sign-red" x1="0" y1="0" x2="0" y2="1">
          <stop offset="0" stop-color="#ec1f27"/>
          <stop offset="1" stop-color="#b20d18"/>
        </linearGradient>
      </defs>
      <rect class="sign-field" width="1100" height="826" fill="url(#sign-red)"/>
      <path class="sign-swoosh-line" d="M0 706 Q550 526 1100 678" fill="none" stroke="#ffffff" stroke-width="4"/>
      <path class="sign-footer" d="M0 742 Q550 566 1100 718 L1100 826 L0 826 Z" fill="#ffffff"/>
      <g class="call-icon" transform="translate(550 610)">
        <circle r="54" fill="#ffffff"/>
        <circle r="45" fill="#c8131e"/>
        <circle r="37" fill="none" stroke="#ffffff" stroke-width="3"/>
        <path d="M-18 -20 l10 -4 l8 14 l-7 6 q5 11 15 16 l6 -7 l14 8 l-4 10 q-4 6 -12 4 q-30 -10 -36 -35 q-1 -9 6 -12 z" fill="#ffffff"/>
        <path d="M6 -22 q14 2 17 17 M6 -32 q24 3 27 27" fill="none" stroke="#ffffff" stroke-width="3" stroke-linecap="round"/>
      </g>
    </svg>

    <div class="sign-content">
      <p class="school-name">KORBANE SCHOOL</p>
      <h1 class="headline">OPEN HOUSE!</h1>
      <svg class="date-icon" viewBox="0 0 80 80" aria-hidden="true">
        <circle cx="40" cy="40" r="37" fill="none" stroke="#ffffff" stroke-width="3"/>
        <rect x="22" y="26" width="36" height="30" rx="3" fill="none" stroke="#ffffff" stroke-width="4"/>
        <rect x="22" y="26" width="36" height="8" fill="#ffffff"/>
        <rect x="29" y="20" width="4" height="10" rx="2" fill="#ffffff"/>
        <rect x="47" y="20" width="4" height="10" rx="2" fill="#ffffff"/>
        <g fill="#ffffff">
          <rect x="29" y="39" width="5" height="4"/><rect x="37.5" y="39" width="5" height="4"/><rect x="46" y="39" width="5" height="4"/>
          <rect x="29" y="46" width="5" height="4"/><rect x="37.5" y="46" width="5" height="4"/><rect x="46" y="46" width="5" height="4"/>
        </g>
      </svg>
      <ul class="dates">
        <li>FEB 10 <sup>TH</sup></li>
        <li>MARCH 10<sup>TH</sup> &amp;</li>
        <li>APRIL 21<sup>ST</sup></li>
      </ul>
      <p class="phone-number">555 014-2967</p>
    </div>
  </section>
</body>
</html>
```